Rack Card Design Project

We are a locally family owned public golf course. We would like to have a rack card designed that can be used for multiple applications. The colors in our logo are grey, blue, and white. Please use those in the card design. The company logo, contact information, address, and summer pricing should be included. I've included some pictures that may or may not be used. I'm also open to suggestions....use one photo, multiple photos, a stock photo or image representing golf etc.

```html
<!DOCTYPE html>
<html lang="en">
<head>
<meta charset="utf-8">
<title>Summer Rates Rack Card</title>
<link href="https://fonts.googleapis.com/css2?family=Oswald:wght@500;600&family=Source+Sans+3:wght@400;700&display=swap" rel="stylesheet">
<style>
  :root {
    --navy: #0f2a55;
    --blue: #1b4f9c;
    --blue-bright: #2160b8;
    --grey: #8a8d92;
    --grey-dark: #4b4f55;
    --text: #2b2b2b;
    --white: #ffffff;
    --sky-top: #b9bcc0;
    --sky-mid: #d9d2c4;
    --grass: #4c6b34;
    --grass-dark: #2f4a22;
  }
  * { box-sizing: border-box; margin: 0; padding: 0; }
  html, body { width: 708px; height: 1200px; overflow: hidden; background: #ffffff; }
  .rack-card {
    position: relative; width: 708px; height: 1200px; overflow: hidden;
    background: linear-gradient(180deg, #ffffff 60%, #eef2f7 100%);
    font-family: "Source Sans 3", Arial, sans-serif; color: var(--text);
  }
  .hero-photo {
    position: absolute; left: 0; top: 0; width: 708px; height: 730px;
    background: linear-gradient(180deg, var(--sky-top) 0%, #cfcfcc 30%, var(--sky-mid) 52%, #6d7f4a 66%, var(--grass) 80%, var(--grass-dark) 100%);
  }
  .hero-swoosh { position: absolute; left: 0; top: 640px; width: 708px; height: 120px; }
  .title {
    position: absolute; top: 52px; width: 100%; text-align: center;
    font-family: "Oswald", Impact, sans-serif; font-weight: 600; font-size: 78px; line-height: 1;
    color: var(--white); letter-spacing: 1px; text-shadow: 0 2px 6px rgba(0,0,0,.35);
  }
  .season {
    position: absolute; top: 148px; width: 100%; text-align: center;
    font-family: "Oswald", Impact, sans-serif; font-weight: 600; font-size: 34px; color: var(--navy);
  }
  .club-mark {
    position: absolute; left: 418px; top: 738px; width: 280px;
    display: flex; align-items: center; gap: 12px;
  }
  .club-mark .dot { width: 34px; height: 34px; border-radius: 50%; background: var(--navy); flex: none; }
  .club-mark .name {
    font-family: "Oswald", Impact, sans-serif; font-weight: 500; font-size: 24px; line-height: 1.15;
    color: var(--navy); text-transform: uppercase;
  }
  .rate-tab {
    position: absolute; left: 0; height: 40px; padding-left: 40px;
    background: linear-gradient(90deg, var(--navy), var(--blue-bright));
    border-radius: 0 20px 20px 0; color: var(--white);
    font-family: "Oswald", Impact, sans-serif; font-weight: 500; font-size: 27px; line-height: 40px; letter-spacing: .5px;
    box-shadow: 0 2px 4px rgba(0,0,0,.25);
  }
  .tab-18 { top: 745px; width: 355px; }
  .tab-9 { top: 912px; width: 355px; }
  .rate-list { position: absolute; left: 38px; list-style: none; font-size: 23px; }
  .rate-list li { display: flex; width: 250px; height: 34px; align-items: baseline; }
  .rate-list .time { white-space: nowrap; }
  .rate-list .leader { flex: 1; border-bottom: 2px dotted var(--text); margin: 0 3px; transform: translateY(-5px); }
  .rate-list .price { font-weight: 700; }
  .rates-18 { top: 795px; }
  .rates-9 { top: 962px; }
  .kids-note {
    position: absolute; left: 430px; top: 832px; width: 260px; text-align: center;
    font-family: "Oswald", Impact, sans-serif; font-weight: 500; font-size: 27px; line-height: 1.35;
    color: var(--navy); text-transform: uppercase; letter-spacing: .5px;
  }
  .lunch {
    position: absolute; left: 38px; top: 1005px;
    font-family: "Oswald", Impact, sans-serif; font-weight: 500; font-size: 26px; color: var(--grey-dark); letter-spacing: .5px;
  }
  .address-band {
    position: absolute; left: 0; top: 1052px; width: 708px; height: 86px;
    background: linear-gradient(90deg, var(--blue) 0%, var(--navy) 100%);
    color: var(--white); text-align: center; font-size: 25px; line-height: 1.35; padding-top: 9px;
    box-shadow: 0 3px 6px rgba(0,0,0,.3); font-style: normal;
  }
  .contact-row {
    position: absolute; left: 0; top: 1150px; width: 708px; display: flex; justify-content: center; gap: 68px;
    font-family: "Oswald", Impact, sans-serif; font-weight: 500; font-size: 27px; color: var(--navy);
  }
  .contact-item { display: flex; align-items: center; gap: 12px; }
  .contact-item svg { width: 34px; height: 34px; }
</style>
</head>
<body>
<main class="rack-card">
  <div class="hero-photo" role="img" aria-label="Photo of a golfer in a pink shirt addressing the ball on a fairway lined with tall pines under an evening sky"></div>
  <svg class="hero-swoosh" viewBox="0 0 708 120" preserveAspectRatio="none" aria-hidden="true">
    <path d="M0 40 C 180 110, 460 70, 708 20 L708 120 L0 120 Z" fill="var(--blue)"/>
    <path d="M0 62 C 190 120, 470 80, 708 38 L708 120 L0 120 Z" fill="#ffffff"/>
  </svg>

  <h1 class="title">SUMMER RATES</h1>
  <p class="season">MAY 1 - SEPTEMBER 30</p>

  <div class="club-mark">
    <span class="dot"></span>
    <span class="name">The Dunes of Pine Hollow Golf Club</span>
  </div>

  <h2 class="rate-tab tab-18">18 HOLES WITH CART</h2>
  <ul class="rate-list rates-18">
    <li><span class="time">7am – 11am</span><span class="leader"></span><span class="price">$24</span></li>
    <li><span class="time">11am – 3pm</span><span class="leader"></span><span class="price">$19</span></li>
    <li><span class="time">3pm – close</span><span class="leader"></span><span class="price">$15</span></li>
  </ul>

  <p class="kids-note">Children 15 and<br>under free with<br>paid adult</p>

  <h2 class="rate-tab tab-9">9 HOLES WITH CART $15</h2>
  <ul class="rate-list rates-9">
    <li><span class="time">Walking</span><span class="leader"></span><span class="price">$12</span></li>
  </ul>

  <p class="lunch">LUNCH AVAILABLE DAILY: 10AM – 3PM</p>

  <address class="address-band">
    The Dunes of Pine Hollow Golf Club<br>
    2450 SW Heron Bay Rd Palm City, FL 34990
  </address>

  <div class="contact-row">
    <span class="contact-item">
      <svg viewBox="0 0 34 34" aria-hidden="true"><circle cx="17" cy="17" r="16" fill="var(--navy)"/><path d="M12 9c1 0 3 3 3 4s-2 1.5-1.5 3 3 4.5 4.5 4.5 2-1.5 3-1.5 4 2 4 3-2 3-4 3c-5 0-12-7-12-12 0-2 2-4 3-4z" fill="#fff"/></svg>
      555-014-2763
    </span>
    <span class="contact-item">
      <svg viewBox="0 0 34 34" aria-hidden="true"><circle cx="17" cy="17" r="16" fill="var(--navy)"/><g fill="none" stroke="#fff" stroke-width="1.8"><circle cx="17" cy="17" r="9"/><ellipse cx="17" cy="17" rx="4" ry="9"/><path d="M8 17h18M10 12h14M10 22h14"/></g></svg>
      PINEHOLLOWGC.COM
    </span>
  </div>
</main>
</body>
</html>
```